Meridian Handsets business card design

I would like to see some designs for a business card for Meridian Handsets. I would like the business card to be double sided. It will need to have a similar colour / look and feel to our website www.meridianhandsets.com.au I have also attached our latest flyer. Final designs to be handed over in Photoshop format so that I can edit the business card when needed please.

Industry/Entity Type

Business

Contact Information for Business Card

Gavin Thornley
sales@meridianhandsets.com.au
Business Development Manager
ph: (08) 6197 5821
www.meridianhandsets.com.au

Font styles to use
Serif
Sans Serif

Requirements
Must have
• If you could please utilise our colour scheme as seen on our website and the attached flyer.
• I would also like the final design to be in a Photoshop format so that I can edit it when needed please.

```html
<!DOCTYPE html>
<html lang="en">
<head>
<meta charset="utf-8">
<title>Meridian Handsets – Business Card</title>
<link rel="stylesheet" href="https://fonts.googleapis.com/css2?family=Open+Sans:ital,wght@0,400;0,600;1,400;1,600&display=swap">
<style>
  :root {
    --brand-blue: #0b7fb9;
    --ink: #333333;
    --rule-dark: #2b2b2b;
    --paper: #ffffff;
    --backdrop: #4a4a4a;
  }
  * { margin: 0; padding: 0; box-sizing: border-box; }
  html, body {
    width: 1105px;
    height: 1200px;
    overflow: hidden;
    background: var(--backdrop);
    font-family: "Open Sans", Arial, sans-serif;
  }
  .sheet {
    position: relative;
    width: 1105px;
    height: 1200px;
  }
  .card {
    position: absolute;
    left: 192px;
    width: 720px;
    height: 412px;
    overflow: hidden;
  }
  .card--front { top: 146px; background: var(--paper); }
  .card--back { top: 602px; background: var(--brand-blue); }

  .front__band {
    position: absolute;
    left: 0; top: 0;
    width: 100%;
    height: 110px;
    background: var(--brand-blue);
    color: var(--paper);
    text-align: center;
  }
  .front__rule {
    position: absolute;
    left: 0; top: 113px;
    width: 100%;
    height: 3px;
    background: var(--rule-dark);
  }
  .holder-name {
    position: absolute;
    top: 26px; left: 0; width: 100%;
    font-size: 27px;
    font-weight: 600;
    line-height: 1;
  }
  .holder-role {
    position: absolute;
    top: 63px; left: 0; width: 100%;
    font-size: 18px;
    font-weight: 400;
    line-height: 1;
  }
  .wordmark {
    position: absolute;
    left: 0; width: 100%;
    text-align: center;
    font-weight: 600;
    line-height: 1;
    letter-spacing: -0.5px;
  }
  .wordmark--front {
    top: 188px;
    font-size: 54px;
    color: var(--ink);
  }
  .contact {
    position: absolute;
    left: 0; width: 100%;
    text-align: center;
    font-size: 18px;
    color: var(--ink);
    line-height: 1;
  }
  .contact--lines { top: 318px; }
  .contact--web { top: 346px; }
  .contact__label {
    color: var(--brand-blue);
    font-weight: 600;
    margin-right: 4px;
  }
  .contact__item + .contact__item { margin-left: 12px; }

  .wordmark--back {
    top: 160px;
    font-size: 50px;
    color: var(--paper);
  }
  .back__web {
    position: absolute;
    top: 350px; left: 0; width: 100%;
    text-align: center;
    color: var(--paper);
    font-size: 17px;
    font-style: italic;
    letter-spacing: 3px;
    line-height: 1;
  }
  .back__web strong { font-weight: 600; }
</style>
</head>
<body>
<main class="sheet">
  <section class="card card--front" aria-label="Card front">
    <header class="front__band">
      <p class="holder-name">Gavin Thornley</p>
      <p class="holder-role">Business Development Manager</p>
    </header>
    <div class="front__rule"></div>
    <p class="wordmark wordmark--front">Meridian Handsets</p>
    <p class="contact contact--lines">
      <span class="contact__item"><span class="contact__label">P :</span>(08) 6197 5821</span>
      <span class="contact__item"><span class="contact__label">E :</span>sales@meridianhandsets.com.au</span>
    </p>
    <p class="contact contact--web">www.meridianhandsets.com.au</p>
  </section>

  <section class="card card--back" aria-label="Card back">
    <p class="wordmark wordmark--back">Meridian Handsets</p>
    <p class="back__web">www.<strong>meridianhandsets</strong>.com.au</p>
  </section>
</main>
</body>
</html>
```